Boutique holiday accommodation signage per house

I am looking for a sign to go out the front of my holiday rentals. I have just started the business and i have lots of competition so i want these signs to stand out but be elegant and modern. I need the signs to be the same but a spot for the house name to be able to be changed by me i photoshop.
Happy for suggestions of any kind.. My logo has pink in it and this is the only pink i want on the sign, happy for otherr colour suggestions but no more pink and no love hearts.
Shape - i would like to see both rectangle and circle designs
Information that needs to be on the sign

Logo - attached (can be white or black)
phone - 0491 306 284
website - www.wrenmoss.com.au
House name - The Gables (use this one for submission)
Beachfront accommodation

if you want to add property icons like shower, beds etc feel free

We live in a beachside town called Robe and its seasonal, so we are mainly accommodatio so i need to stick out!!

Target Market(s)

All ages there isnt really one - people looking for accomodation whilst driving

Industry/Entity Type

Tourism

Font styles to use
Sans Serif
Script

Requirements
Must have
• Logo - attached (can be white or black)
• phone - 0491 306 284
• website - www.wrenmoss.com.au
• House name - The Gables (use this one for submission)
• Beachfront accommodation
• i want creatvity so use your imagination
Should not have
• no hearts
• no pink

```html
<!DOCTYPE html>
<html lang="en">
<head>
<meta charset="UTF-8">
<title>The Gables – Beachfront Accommodation Sign</title>
<link rel="stylesheet" href="https://fonts.googleapis.com/css2?family=Dancing+Script:wght@500;600&family=Josefin+Slab:wght@600&family=Arimo:wght@400;700&display=swap">
<style>
  :root {
    --teal: #4f8699;
    --orange: #d0632f;
    --ink: #111111;
    --logo-ink: #231f20;
    --muted: #6d6a6a;
    --paper: #ffffff;
    --sky-top: #3f7fc4;
    --sky-low: #a9cbe6;
    --sea: #2f9aa8;
    --sea-deep: #1f7791;
    --sand: #cdbfa3;
    --scrub: #6f8c4a;
    --scrub-dark: #4c6a35;
  }
  * { box-sizing: border-box; margin: 0; padding: 0; }
  html, body { width: 1200px; height: 1000px; overflow: hidden; background: var(--paper); }
  .sign { position: relative; width: 1200px; height: 1000px; background: var(--paper); }

  .hero {
    position: absolute; left: 0; top: 0; width: 1200px; height: 460px;
    background: linear-gradient(180deg,
      var(--sky-top) 0%, #6ea3d4 22%, var(--sky-low) 48%,
      var(--sea) 56%, var(--sea-deep) 66%, #5aa9b0 72%,
      var(--sand) 76%, #b7a98a 80%, var(--scrub) 86%, var(--scrub-dark) 100%);
  }
  .hero__pin { position: absolute; left: 518px; top: 68px; width: 165px; height: 222px; }

  .tagline-top {
    position: absolute; top: 514px; left: 0; width: 1200px; text-align: center;
    font-family: "Josefin Slab", serif; font-weight: 600; font-size: 22px;
    letter-spacing: 5px; color: var(--orange);
  }
  .headline {
    position: absolute; top: 478px; left: 0; width: 1200px; text-align: center;
    font-family: "Dancing Script", cursive; font-weight: 600; font-size: 190px;
    line-height: 1; color: var(--teal);
  }
  .service {
    position: absolute; top: 668px; left: 0; width: 1200px; text-align: center;
    font-family: "Josefin Slab", serif; font-weight: 600; font-size: 29px;
    letter-spacing: 5px; color: var(--orange); text-transform: uppercase;
  }
  .service__dot { font-size: 22px; vertical-align: 4px; letter-spacing: 0; }
  .house-name {
    position: absolute; top: 738px; left: 0; width: 1200px; text-align: center;
    font-family: "Dancing Script", cursive; font-weight: 500; font-size: 56px;
    line-height: 1; color: var(--teal);
  }
  .address {
    position: absolute; top: 812px; left: 292px;
    font-family: "Arimo", sans-serif; font-weight: 700; font-size: 25px; color: var(--ink);
  }

  .brand { position: absolute; left: 295px; top: 893px; width: 282px; }
  .brand__name {
    font-family: "Arimo", sans-serif; font-weight: 700; font-size: 50px;
    line-height: 1; letter-spacing: -1px; color: var(--logo-ink); white-space: nowrap;
  }
  .brand__descriptor {
    margin-top: 6px; font-family: "Arimo", sans-serif; font-weight: 400;
    font-size: 17px; color: var(--muted); letter-spacing: 0.3px;
  }

  .contact { position: absolute; left: 626px; top: 903px; list-style: none; }
  .contact__item {
    display: flex; align-items: center; gap: 12px; height: 29px;
    font-family: "Arimo", sans-serif; font-size: 26px; color: var(--ink);
  }
  .contact__item--phone { font-weight: 700; }
  .contact__icon { width: 22px; height: 22px; flex: none; }
</style>
</head>
<body>
<main class="sign">
  <div class="hero" role="img" aria-label="Photograph of a sunny bay in Robe: turquoise water, a sandy beach, coastal scrub in the foreground and a rocky headland with houses under a blue sky">
    <svg class="hero__pin" viewBox="0 0 165 222" aria-hidden="true">
      <path fill="#ffffff" fill-rule="evenodd"
        d="M82.5 0C37 0 0 37 0 82.5c0 48 52 103 82.5 139.5C113 185.5 165 130.5 165 82.5 165 37 128 0 82.5 0Z
           M82.5 38a35 35 0 1 0 0.01 0Z"/>
    </svg>
  </div>

  <p class="tagline-top">YOUR NEXT</p>
  <h1 class="headline">Adventure</h1>
  <p class="service"><span class="service__dot">•</span>Beachfront accommodation<span class="service__dot">•</span></p>
  <h2 class="house-name">The Gables</h2>
  <p class="address">24 Saltbush Road, Robe South Australia</p>

  <div class="brand">
    <div class="brand__name">WREN MOSS</div>
    <div class="brand__descriptor">property &amp; events management</div>
  </div>

  <ul class="contact">
    <li class="contact__item contact__item--phone">
      <svg class="contact__icon" viewBox="0 0 24 24" aria-hidden="true">
        <circle cx="12" cy="12" r="11" fill="var(--ink)"/>
        <path fill="#fff" d="M8.6 6.2l1.6-.4 1.3 2.9-1.1 1c.6 1.4 1.6 2.5 3 3.2l1-1.1 2.9 1.3-.4 1.6c-.2.7-.9 1.2-1.6 1.1-4-.6-7.3-3.9-7.9-7.9-.1-.7.4-1.4 1.2-1.7Z"/>
      </svg>
      0491 306 284
    </li>
    <li class="contact__item">
      <svg class="contact__icon" viewBox="0 0 24 24" aria-hidden="true">
        <circle cx="12" cy="12" r="11" fill="var(--ink)"/>
        <g fill="none" stroke="#fff" stroke-width="1.4">
          <circle cx="12" cy="12" r="7"/>
          <ellipse cx="12" cy="12" rx="3.2" ry="7"/>
          <line x1="5" y1="12" x2="19" y2="12"/>
          <path d="M6.2 8.5h11.6M6.2 15.5h11.6"/>
        </g>
      </svg>
      www.wrenmoss.com.au
    </li>
  </ul>
</main>
</body>
</html>
```